Creative Out of the Box Post Up Banner Needed

I am looking for a great design for my banner. The design will be printed on a retractable vertical banner. Size 80 inches X 32 inches.

It will be displayed at my seminar and industry trade shows.

It needs to position me as a celebrity expert to grab people's attention. It shouldn't look boring.

Imagine a banner for a celebrity or a rock star.

It should look high-end and elegant.

The banner should include the entire body from head to toe, that makes it life-size when I print the banner.

Target Market(s)

salon and spa owners

Industry/Entity Type

Industry

Requirements
Must have
• My photo and a small book cover image.

You can download the images from:
http://www.glowtradecoach.com/images/bannerphoto.jpg
http://www.glowtradecoach.com/images/bookcover.jpg

Text that on the banner.

"Successful, rich, happy owners aren't smarter. They just play by a different set of rules."

Ivo Venn
#1 Business Expert In The Salon & Spa Industry
Millionaire Salon Owner
Best-Selling Author of Quiet Habits Of Parlor Keepers And A Ladder Out Of Debt
Nice to have
• Designs that I like.
http://www.artpitchhub.com/design/69852/poster-design-other-by-lumenpixo
http://mint-lantern.co.kr/pds/board/201108/poster.jpg
http://herbookedchairs.com/wp-content/uploads/2009/11/P10101561.jpg

```html
<!DOCTYPE html>
<html lang="en">
<head>
<meta charset="utf-8">
<title>Ivo Venn – Retractable Banner</title>
<link rel="stylesheet" href="https://fonts.googleapis.com/css2?family=Varela+Round&family=Didact+Gothic&family=Arimo:wght@400;700&family=Tinos&display=swap">
<style>
  :root {
    --paper: #ffffff;
    --quote-panel: #ecd9e1;
    --magenta: #c4237f;
    --ink: #111111;
    --ink-soft: #222222;
    --author-green: #2f7a1c;
    --mauve: #8e4a6c;
    --plum: #3a1024;
    --night: #0d0508;
    --floor-line: #b65a88;
    --bokeh: #a4507c;
  }
  * { box-sizing: border-box; margin: 0; padding: 0; }
  html, body { width: 1200px; height: 3000px; overflow: hidden; }
  body { background: var(--paper); font-family: "Arimo", Arial, sans-serif; }

  .banner {
    position: relative;
    width: 1200px;
    height: 3000px;
    overflow: hidden;
    background: linear-gradient(to bottom,
      var(--paper) 0px,
      var(--paper) 960px,
      #d9bccb 1060px,
      var(--mauve) 1160px,
      var(--plum) 1290px,
      #1b0810 1700px,
      var(--night) 3000px);
  }

  .backdrop { position: absolute; inset: 0; z-index: 0; }

  .quote-panel {
    position: absolute;
    left: 54px; top: 45px;
    width: 1112px; height: 465px;
    background: var(--quote-panel);
    border-radius: 28px;
    padding: 36px 0 0 24px;
    font-family: "Varela Round", Arial, sans-serif;
    color: var(--magenta);
    z-index: 3;
  }
  .quote-line { display: block; white-space: nowrap; line-height: 1.08; }
  .quote-line--lead { font-size: 66px; }
  .quote-line--punch { font-size: 86px; }
  .quote-line--gap { margin-top: 24px; }

  .identity {
    position: absolute;
    left: 54px; top: 528px;
    z-index: 3;
  }
  .identity__name {
    font-family: "Didact Gothic", Arial, sans-serif;
    font-size: 156px;
    font-weight: 400;
    -webkit-text-stroke: 3px var(--ink);
    color: var(--ink);
    line-height: 1;
    letter-spacing: 2px;
  }
  .identity__title {
    margin-top: 14px;
    font-size: 42px;
    font-weight: 700;
    color: var(--ink-soft);
    white-space: nowrap;
  }
  .identity__role {
    margin-top: 10px;
    font-size: 32px;
    font-weight: 700;
    color: var(--ink-soft);
  }
  .identity__author-label {
    margin-top: 52px;
    font-size: 36px;
    color: var(--author-green);
  }
  .identity__book-title {
    margin-top: 6px;
    font-family: "Tinos", Georgia, serif;
    font-size: 32px;
    color: var(--ink);
    white-space: nowrap;
  }

  .book-cover {
    position: absolute;
    left: 54px; top: 940px;
    width: 270px; height: 395px;
    background: linear-gradient(to bottom, #2f6e1f 0 9%, #f4f1e8 9% 90%, #2f6e1f 90% 100%);
    box-shadow: 8px 8px 20px rgba(0,0,0,0.35);
    z-index: 2;
  }

  .portrait {
    position: absolute;
    left: 560px; top: 945px;
    width: 620px; height: 2020px;
    background: linear-gradient(to bottom, #2a1b1f 0%, #141014 40%, #1c1a1c 100%);
    border-radius: 260px 260px 40px 40px;
    z-index: 1;
  }
</style>
</head>
<body>
<main class="banner">
  <svg class="backdrop" width="1200" height="3000" viewBox="0 0 1200 3000" aria-hidden="true">
    <g class="bokeh" fill="var(--bokeh)">
      <circle cx="270" cy="1470" r="180" opacity="0.45"/>
      <circle cx="465" cy="1740" r="186" opacity="0.35"/>
      <circle cx="240" cy="2220" r="165" opacity="0.3"/>
      <circle cx="426" cy="2154" r="84" opacity="0.4"/>
    </g>
    <path class="floor-line" d="M0 2715 Q 600 2520 1200 2590" fill="none" stroke="var(--floor-line)" stroke-width="3" opacity="0.8"/>
  </svg>

  <blockquote class="quote-panel">
    <span class="quote-line quote-line--lead">"Successful, rich, happy owners</span>
    <span class="quote-line quote-line--punch">aren't smarter.</span>
    <span class="quote-line quote-line--lead quote-line--gap">They just play</span>
    <span class="quote-line quote-line--punch">by a different set of rules."</span>
  </blockquote>

  <header class="identity">
    <h1 class="identity__name">Ivo Venn</h1>
    <p class="identity__title">#1 Business Expert In The Salon &amp; Spa Industry</p>
    <p class="identity__role">Millionaire Salon Owner</p>
    <p class="identity__author-label">Best-Selling Author of</p>
    <p class="identity__book-title">Quiet Habits Of Parlor Keepers And A Ladder Out Of Debt</p>
  </header>

  <div class="book-cover" role="img" aria-label="Book cover: Quiet Habits Of Parlor Keepers And A Ladder Out Of Debt"></div>

  <div class="portrait" role="img" aria-label="Full-length photo of Ivo Venn in a black velvet suit, arms crossed, standing life-size"></div>
</main>
</body>
</html>
```